Driftwood Bay Private Yacht Charter "Rack Flyer"

This will be a 4" x 9" Rack flyer that is 4 colors and two sided. This is a Private Yacht charter company that is based in St Thomas, U.S. Virgin Islands. Our main product that I would like to promote on one entire side of the flyer is our Private Luxury Full Day "Gilded Galley". our charter company is unique in the fact we offer customizable itineraries and we offer unique activities that keep the family and groups engaged in fun for the entire day. We would like something with our colors.

Target Market(s)

We are trying to reach an upscale clients that are looking for a Luxury Day Charter experience. these people will be most likely staying in Private Villas or staying at the Halloway Crest or PK Bellmont.

Requirements
Must have
• Contact Information:
Ph: (340) 555-0187
email: Info@driftwoodbayvoyages.example
www.driftwoodbayvoyages.example
One side should Promote our Gilded Galley (Gilded Galley is a trademarked name).
All Guests will receive "Harbor Fizz"
> Up to 12 guests
> Full Brunch Spread to include, Assorted fruit tower, Artesian Waffle Board, Frittata's, Loaded Avocado Toast or an All American Breakfast.
> Specialty Cocktails with Bottle Service options available
List all of our Unique activities to include:
Snorkeling
Underwater WaveGlider
Cliff Diving
Paddleboarding
Towable Activities
TEXT TO BE WRITTEN:
Experience yacht charter service at its Finest!
Sail away with us on a Luxury Charter experience complete with a full brunch spread. During our sail we will take you to the hottest destination spots in the Caribbean surrounding St Thomas and St John. Warm, fresh baked afternoon cookies will be served on the way back from our days journeys. Unlimited water, sodas, beer and rum punch will be provided for the entire group to enjoy throughout the day.
_________________

On side two of the brochure you can refer to the downloaded text. We do not want pricing listed on the flyer

```html
<!DOCTYPE html>
<html lang="en">
<head>
<meta charset="utf-8">
<title>Driftwood Bay Private Yacht Charter – Gilded Galley Rack Flyer</title>
<link rel="stylesheet" href="https://fonts.googleapis.com/css2?family=Bebas+Neue&family=Poppins:wght@400;500;600;700&display=swap">
<style>
  :root {
    --brand-blue: #0d55a6;
    --brand-red: #e8202a;
    --ink: #1d1d1f;
    --body-ink: #3b3b3d;
    --paper: #ffffff;
    --canvas: #ffffff;
  }
  * { box-sizing: border-box; margin: 0; padding: 0; }
  html, body {
    width: 1145px; height: 1200px; overflow: hidden;
    background: var(--canvas);
    font-family: "Poppins", Arial, sans-serif;
    color: var(--ink);
  }
  .flyer {
    position: absolute; top: 89px;
    width: 453px; height: 1019px;
    background: var(--paper);
    overflow: hidden;
  }
  .flyer--front { left: 52px; }
  .flyer--back { left: 608px; }
  .flyer__art { position: absolute; inset: 0; width: 453px; height: 1019px; }

  .brand-name {
    position: absolute; top: 40px; left: 0; width: 100%;
    text-align: center;
    font-family: "Poppins", Arial, sans-serif;
    font-weight: 600; font-size: 34px; letter-spacing: 1px;
    color: var(--paper);
  }

  .bullet-list { list-style: none; }
  .bullet-list li { position: relative; padding-left: 19px; }
  .bullet-list li::before {
    content: ""; position: absolute; left: 2px; top: 0.5em;
    width: 6px; height: 6px; border-radius: 50%;
    background: var(--brand-red);
  }

  /* Front */
  .promo-title {
    position: absolute; left: 48px; top: 514px;
    font-family: "Bebas Neue", "Arial Narrow", sans-serif;
    font-size: 74px; line-height: 62px; letter-spacing: 0.5px;
  }
  .promo-title__top { display: block; color: var(--brand-red); }
  .promo-title__bottom { display: block; color: var(--brand-blue); }

  .perks {
    position: absolute; left: 48px; top: 652px; width: 320px;
    font-size: 10.2px; line-height: 13px; color: var(--ink);
  }
  .perks li { margin-bottom: 3.5px; }

  .activities-label {
    position: absolute; left: 47px; top: 756px;
    width: 313px; height: 23px; border-radius: 3px;
    background: var(--brand-blue); color: var(--paper);
    font-size: 12.6px; font-weight: 600; line-height: 23px;
    padding-left: 20px;
  }
  .activities {
    position: absolute; left: 48px; top: 788px; width: 380px;
    display: flex;
    font-size: 13.2px; line-height: 17px; color: var(--ink);
  }
  .activities .bullet-list:first-child { width: 171px; }

  .finest {
    position: absolute; left: 48px; top: 851px; width: 380px;
    font-size: 15.2px; font-weight: 700; color: var(--ink);
  }
  .finest-copy {
    position: absolute; left: 48px; top: 876px; width: 369px;
    font-size: 9.7px; line-height: 13.4px; text-align: justify;
    color: var(--body-ink);
  }

  .contact-bar {
    position: absolute; left: 0; bottom: 0; width: 100%; height: 54px;
    background: var(--brand-red); color: var(--paper);
    text-align: center; font-size: 11px; line-height: 16px;
    padding-top: 10px; white-space: nowrap;
  }
  .contact-bar__phone { font-size: 12.4px; }
  .contact-bar__row .divider { margin: 0 14px; }

  /* Back */
  .story {
    position: absolute; left: 43px; top: 585px; width: 368px;
    font-size: 9.7px; line-height: 13.4px; color: var(--body-ink);
  }
  .story p { text-align: justify; }
  .menu {
    margin: 8px 0 6px 2px;
    font-size: 9.9px; line-height: 16.5px; color: var(--ink);
  }
  .menu li { padding-left: 16px; }
</style>
</head>
<body>

<section class="flyer flyer--front" aria-label="Gilded Galley front side">
  <svg class="flyer__art" viewBox="0 0 742 1670" preserveAspectRatio="none">
    <defs>
      <linearGradient id="seaAerial" x1="0" y1="0" x2="1" y2="1">
        <stop offset="0" stop-color="#1f9fb9"/>
        <stop offset="0.55" stop-color="#4fc2cf"/>
        <stop offset="1" stop-color="#b9e6e6"/>
      </linearGradient>
      <radialGradient id="shallows" cx="0.5" cy="0.5" r="0.6">
        <stop offset="0" stop-color="#d9eef0"/>
        <stop offset="0.6" stop-color="#9fd8dc"/>
        <stop offset="1" stop-color="#5f9fae"/>
      </radialGradient>
    </defs>
    <rect class="header-band" x="0" y="0" width="742" height="900" fill="var(--brand-blue)"/>
    <path role="img" aria-label="Aerial photo of a catamaran anchored in turquoise surf"
          d="M0 165 Q 480 160 742 392 V 900 H0 Z" fill="url(#seaAerial)"/>
    <path class="panel-white" d="M0 837 Q 400 790 742 632 V1670 H0 Z" fill="var(--paper)"/>
    <circle cx="514" cy="745" r="217" fill="var(--paper)"/>
    <circle role="img" aria-label="Photo of a snorkeler swimming with stingrays over white sand"
            cx="514" cy="745" r="200" fill="url(#shallows)"/>
  </svg>

  <div class="brand-name">Driftwood Bay</div>

  <h1 class="promo-title">
    <span class="promo-title__top">Gilded</span>
    <span class="promo-title__bottom">Galley</span>
  </h1>

  <ul class="perks bullet-list">
    <li>All Guests will receive "Harbor Fizz"</li>
    <li>Up to 12 guests</li>
    <li>Full Brunch Spread to include, Assorted fruit tower,<br>Artesian Waffle Board, Frittata's, Loaded Avocado<br>Toast or an All American Breakfast.</li>
    <li>Specialty Cocktails with Bottle Service options available</li>
  </ul>

  <div class="activities-label">List all of our Unique activities to include:</div>
  <div class="activities">
    <ul class="bullet-list">
      <li>Snorkeling</li>
      <li>Cliff Diving</li>
      <li>Towable Activities</li>
    </ul>
    <ul class="bullet-list">
      <li>Underwater WaveGlider</li>
      <li>Paddleboarding</li>
    </ul>
  </div>

  <h2 class="finest">Experience yacht charter service at its Finest!</h2>
  <p class="finest-copy">Sail away with us on a Luxury Charter experience complete with a full brunch spread. During our sail we will take you to the hottest destination spots in the Caribbean surrounding St Thomas and St John. Warm, fresh baked afternoon cookies will be served on the way back from our days journeys. Unlimited water, sodas, beer and rum punch will be provided for the entire group to enjoy throughout the day.</p>

  <footer class="contact-bar">
    <div class="contact-bar__phone">(340) 555-0187</div>
    <div class="contact-bar__row">Info@driftwoodbayvoyages.example<span class="divider">|</span>www.driftwoodbayvoyages.example</div>
  </footer>
</section>

<section class="flyer flyer--back" aria-label="Gilded Galley back side">
  <svg class="flyer__art" viewBox="0 0 742 1670" preserveAspectRatio="none">
    <defs>
      <linearGradient id="seaTurtle" x1="0" y1="0" x2="1" y2="1">
        <stop offset="0" stop-color="#1a8fc4"/>
        <stop offset="0.5" stop-color="#3fbad3"/>
        <stop offset="1" stop-color="#8fd3c9"/>
      </linearGradient>
      <linearGradient id="bayView" x1="0" y1="0" x2="0" y2="1">
        <stop offset="0" stop-color="#9fd0ef"/>
        <stop offset="0.45" stop-color="#2fb7d6"/>
        <stop offset="0.75" stop-color="#3f9a4a"/>
        <stop offset="1" stop-color="#2c7a34"/>
      </linearGradient>
      <linearGradient id="crewToast" x1="0" y1="0" x2="1" y2="0">
        <stop offset="0" stop-color="#b08a6c"/>
        <stop offset="0.5" stop-color="#d8c7b4"/>
        <stop offset="1" stop-color="#9bb1c9"/>
      </linearGradient>
    </defs>
    <rect class="header-band" x="0" y="0" width="742" height="900" fill="var(--brand-blue)"/>
    <path role="img" aria-label="Underwater photo of a sea turtle gliding over seagrass"
          d="M0 165 Q 420 170 742 387 V 900 H0 Z" fill="url(#seaTurtle)"/>
    <path class="panel-white" d="M0 627 Q 340 800 742 837 V1670 H0 Z" fill="var(--paper)"/>
    <path role="img" aria-label="Photo of friends raising cocktails at brunch on deck"
          d="M0 1282 Q 380 1350 742 1338 V1582 H0 Z" fill="url(#crewToast)"/>
    <circle cx="236" cy="745" r="217" fill="var(--paper)"/>
    <circle role="img" aria-label="Photo of a palm-lined bay with white sand beach and green hills"
            cx="236" cy="745" r="200" fill="url(#bayView)"/>
  </svg>

  <div class="brand-name">Driftwood Bay</div>

  <div class="story">
    <p>Our newest addition to our charters is the full day “Gilded Galley.” Driftwood Bay is now one of the only chartering companies that offer a private full day brunch sail. This brunch comes with a plate of your choice and an all you can drink buffet! Some of our brunch menu items include:</p>
    <ul class="menu bullet-list">
      <li>Assorted fruit plate,</li>
      <li>Artesian waffle board with all the extras</li>
      <li>Frittata</li>
      <li>Loaded Avocado toast</li>
      <li>All American Breakfast</li>
    </ul>
    <p>Visit some of the best scenery in the USVI while you enjoy our one of a kind menu. Come join us for an all day brunch spectacular getaway! Our crew will make sure that you have the day of a lifetime. Driftwood Bay!</p>
  </div>

  <footer class="contact-bar">
    <div class="contact-bar__phone">(340) 555-0187</div>
    <div class="contact-bar__row">Info@driftwoodbayvoyages.example<span class="divider">|</span>www.driftwoodbayvoyages.example</div>
  </footer>
</section>

</body>
</html>
```